Velisto Events Business Card

We need a business cards that stands out to our clients. We are company who targets prestige clients to spend money with us on experiences, so our image needs to be prestige
Target Market(s)
Corporate
Contact Information for Business Card
There will be four different names on the business cards
Dana Morrowby
Director
O: 02 5147 3086
M: 0451 692 038
E: info@velistoevents.example.au
Facebook: @velistoevents
Instagram: velistoevents
www.velistoevents.example.au
Nathaniel Morrowby
Director
O: 02 5147 3086
M: 0467 215 904
Facebook: @velistoevents
Instagram: velistoevents
www.velistoevents.example.au
Teodor Vinkel
Director
O: 02 5147 3086
M: 0478 903 527
Facebook: @velistoevents
Instagram: velistoevents
www.velistoevents.example.au
Mabel Hartung
Director
O: 02 5147 3086
Facebook: @velistoevents
Instagram: velistoevents
www.velistoevents.example.au
Colors
Designer to choose colors to be used in the design.
Look and feel

```html
<!DOCTYPE html>
<html lang="en">
<head>
<meta charset="utf-8">
<title>Velisto Events Business Cards</title>
<link href="https://fonts.googleapis.com/css2?family=EB+Garamond:wght@400;500;700&display=swap" rel="stylesheet">
<style>
  :root{
    --page:#ffffff;
    --card:#27224f;
    --band:#150f35;
    --gold:#d8b04a;
    --gold-light:#f6de8c;
    --gold-dark:#a77d22;
    --ink-light:#ffffff;
    --icon:#1e1940;
  }
  *{box-sizing:border-box;margin:0;padding:0}
  html,body{width:1200px;height:1200px;overflow:hidden;background:var(--page)}
  body{font-family:"EB Garamond",Georgia,serif}
  .sheet{
    position:absolute;left:154px;top:52px;
    display:grid;grid-template-columns:434px 434px;grid-auto-rows:261px;
    column-gap:24px;row-gap:21px;
  }
  .card{position:relative;background:var(--card);overflow:hidden}
  .brand{
    position:absolute;left:70px;top:46px;transform:translateX(-50%);
    display:flex;flex-direction:column;align-items:center;gap:10px;
    color:var(--gold);font-weight:500;text-transform:uppercase;text-align:center;
  }
  .brand-mark{width:40px;height:40px;border-radius:50%;border:2px solid var(--gold)}
  .brand-name{font-size:13px;letter-spacing:4px;line-height:1.3;white-space:nowrap}
  .person{position:absolute;right:16px;top:98px;text-align:right}
  .person-name{color:var(--ink-light);font-size:21px;font-weight:500;line-height:1}
  .person-role{color:var(--gold);font-size:9.5px;letter-spacing:.5px;margin-top:4px}
  .tab{
    position:absolute;top:172px;width:40px;height:29px;
    background:linear-gradient(135deg,var(--gold-light),var(--gold) 50%,var(--gold-dark));
    display:flex;align-items:center;justify-content:center;
  }
  .tab-mail{left:0;border-radius:0 15px 15px 0;box-shadow:2px 1px 0 #fff}
  .tab-phone{right:0;border-radius:15px 0 0 15px;box-shadow:-2px 1px 0 #fff}
  .contact{position:absolute;top:176px;color:var(--ink-light);font-size:14px;line-height:20px}
  .contact-mail{left:50px}
  .contact-phone{right:48px;font-size:15px}
  .band{
    position:absolute;left:0;right:0;bottom:0;height:43px;background:var(--band);
    color:var(--ink-light);font-size:12px;display:flex;align-items:center;
  }
  .web{position:absolute;left:35px;font-weight:700;font-size:11.5px}
  .social{position:absolute;left:266px;display:flex;align-items:center;gap:5px}
  .social-dot{width:8px;height:8px;border-radius:50%;background:var(--ink-light)}
  .social-rule{width:1px;height:14px;background:var(--gold);margin:0 4px}
  .back .brand{left:50%;top:74px;gap:14px}
  .back .brand-mark{width:70px;height:70px;border-width:3px}
  .back .brand-name{font-size:21px;letter-spacing:7px}
</style>
</head>
<body>
<main class="sheet">

  <section class="card front">
    <div class="brand"><span class="brand-mark"></span><span class="brand-name">Velisto<br>Events</span></div>
    <div class="person"><p class="person-name">Dana Morrowby</p><p class="person-role">DIRECTOR</p></div>
    <div class="tab tab-mail"><svg width="11" height="9" viewBox="0 0 11 9"><rect x=".6" y=".6" width="9.8" height="7.8" fill="none" stroke="#1e1940" stroke-width="1.2"/><path d="M.8 1l4.7 3.6L10.2 1" fill="none" stroke="#1e1940" stroke-width="1.2"/></svg></div>
    <p class="contact contact-mail">info@velistoevents.example.au</p>
    <p class="contact contact-phone">0451 692 038</p>
    <div class="tab tab-phone"><svg width="9" height="13" viewBox="0 0 9 13"><rect x=".7" y=".7" width="7.6" height="11.6" rx="1.3" fill="none" stroke="#1e1940" stroke-width="1.4"/><rect x="3" y="9.6" width="3" height="1" fill="#1e1940"/></svg></div>
    <div class="band"><span class="web">www.velistoevents.example.au</span><span class="social"><span class="social-dot"></span><span class="social-dot"></span><span class="social-rule"></span>@velistoevents</span></div>
  </section>
  <section class="card back"><div class="brand"><span class="brand-mark"></span><span class="brand-name">Velisto<br>Events</span></div></section>

  <section class="card front">
    <div class="brand"><span class="brand-mark"></span><span class="brand-name">Velisto<br>Events</span></div>
    <div class="person"><p class="person-name">Nathaniel Morrowby</p><p class="person-role">DIRECTOR</p></div>
    <div class="tab tab-mail"><svg width="11" height="9" viewBox="0 0 11 9"><rect x=".6" y=".6" width="9.8" height="7.8" fill="none" stroke="#1e1940" stroke-width="1.2"/><path d="M.8 1l4.7 3.6L10.2 1" fill="none" stroke="#1e1940" stroke-width="1.2"/></svg></div>
    <p class="contact contact-mail">info@velistoevents.example.au</p>
    <p class="contact contact-phone">0467 215 904</p>
    <div class="tab tab-phone"><svg width="9" height="13" viewBox="0 0 9 13"><rect x=".7" y=".7" width="7.6" height="11.6" rx="1.3" fill="none" stroke="#1e1940" stroke-width="1.4"/><rect x="3" y="9.6" width="3" height="1" fill="#1e1940"/></svg></div>
    <div class="band"><span class="web">www.velistoevents.example.au</span><span class="social"><span class="social-dot"></span><span class="social-dot"></span><span class="social-rule"></span>@velistoevents</span></div>
  </section>
  <section class="card back"><div class="brand"><span class="brand-mark"></span><span class="brand-name">Velisto<br>Events</span></div></section>

  <section class="card front">
    <div class="brand"><span class="brand-mark"></span><span class="brand-name">Velisto<br>Events</span></div>
    <div class="person"><p class="person-name">Teodor Vinkel</p><p class="person-role">DIRECTOR</p></div>
    <div class="tab tab-mail"><svg width="11" height="9" viewBox="0 0 11 9"><rect x=".6" y=".6" width="9.8" height="7.8" fill="none" stroke="#1e1940" stroke-width="1.2"/><path d="M.8 1l4.7 3.6L10.2 1" fill="none" stroke="#1e1940" stroke-width="1.2"/></svg></div>
    <p class="contact contact-mail">info@velistoevents.example.au</p>
    <p class="contact contact-phone">0478 903 527</p>
    <div class="tab tab-phone"><svg width="9" height="13" viewBox="0 0 9 13"><rect x=".7" y=".7" width="7.6" height="11.6" rx="1.3" fill="none" stroke="#1e1940" stroke-width="1.4"/><rect x="3" y="9.6" width="3" height="1" fill="#1e1940"/></svg></div>
    <div class="band"><span class="web">www.velistoevents.example.au</span><span class="social"><span class="social-dot"></span><span class="social-dot"></span><span class="social-rule"></span>@velistoevents</span></div>
  </section>
  <section class="card back"><div class="brand"><span class="brand-mark"></span><span class="brand-name">Velisto<br>Events</span></div></section>

  <section class="card front">
    <div class="brand"><span class="brand-mark"></span><span class="brand-name">Velisto<br>Events</span></div>
    <div class="person"><p class="person-name">Mabel Hartung</p><p class="person-role">DIRECTOR</p></div>
    <div class="tab tab-mail"><svg width="11" height="9" viewBox="0 0 11 9"><rect x=".6" y=".6" width="9.8" height="7.8" fill="none" stroke="#1e1940" stroke-width="1.2"/><path d="M.8 1l4.7 3.6L10.2 1" fill="none" stroke="#1e1940" stroke-width="1.2"/></svg></div>
    <p class="contact contact-mail">info@velistoevents.example.au</p>
    <p class="contact contact-phone">0482 306 715</p>
    <div class="tab tab-phone"><svg width="9" height="13" viewBox="0 0 9 13"><rect x=".7" y=".7" width="7.6" height="11.6" rx="1.3" fill="none" stroke="#1e1940" stroke-width="1.4"/><rect x="3" y="9.6" width="3" height="1" fill="#1e1940"/></svg></div>
    <div class="band"><span class="web">www.velistoevents.example.au</span><span class="social"><span class="social-dot"></span><span class="social-dot"></span><span class="social-rule"></span>@velistoevents</span></div>
  </section>
  <section class="card back"><div class="brand"><span class="brand-mark"></span><span class="brand-name">Velisto<br>Events</span></div></section>

</main>
</body>
</html>
```